Internal Designs and HTML Prototype

A Home page design has been completed. The remaining 6 pages need to be designed based on the provided wireframes and the home page design. HTML conversion to be performed to the following standards; - XHTML 1.0 Transitional - Fixed width - Cross-browser compatibility - Safari 2&3, Opera 9 etc - Relative Font sizes - Table-less forms - JQuery as preferred Javascript library - SEO and loading optimoisation

The selected designer will be required to provide the HTML prototype for their layouts.

Target Market(s)

Ensure style of provided Home page is followed.

Industry/Entity Type

Real Estate

```html
<!DOCTYPE html>
<html lang="en">
<head>
<meta charset="utf-8">
<title>TradeNest – Property Search</title>
<link rel="stylesheet" href="https://fonts.googleapis.com/css2?family=Mulish:wght@400;600;700;800&family=Handlee&display=swap">
<style>
:root{
  --page-bg:#dfe9d2;
  --panel-frame:#687565;
  --tab:#7b8a77;
  --tab-text:#ffffff;
  --orange:#f26a1b;
  --red-band-a:#e2361e;
  --red-band-b:#f2552a;
  --grass-a:#4f7a2c;
  --grass-b:#8fb05a;
  --text:#3a3a3a;
  --muted:#8a8a8a;
  --field-border:#9aa39a;
  --field-bg:#f4f4f4;
  --white:#ffffff;
}
*{box-sizing:border-box;margin:0;padding:0}
html,body{width:1200px;height:905px;overflow:hidden}
body{position:relative;background:var(--page-bg);font-family:"Mulish",Arial,sans-serif;color:var(--text)}
.abs{position:absolute}

/* header */
.hero{left:0;top:0;width:1200px;height:210px;background:linear-gradient(160deg,var(--grass-a),var(--grass-b) 55%,#6a9440)}
.brand{left:40px;top:70px;display:flex;align-items:center;gap:14px;color:var(--white);font-size:44px;font-weight:800}
.brand-mark{width:34px;height:34px;background:var(--orange)}
.tagline-band{left:0;top:210px;width:1200px;height:48px;background:linear-gradient(90deg,var(--red-band-a),var(--red-band-b));border-bottom:3px solid #c92c16}
.tagline{left:34px;top:219px;color:var(--white);font-size:27px;font-weight:400}
.login{top:226px;color:var(--white);font-size:10px;font-weight:700;letter-spacing:.5px}
.login-input{top:227px;width:130px;height:17px;background:var(--white);border:1px solid #ddd}
.signin{left:1103px;top:227px;width:64px;height:18px;background:var(--panel-frame);border:1px solid #eee;color:var(--white);font-size:9px;font-weight:700;text-align:center;line-height:16px}

/* navigation */
.nav-tab{left:18px;width:148px;height:80px;background:var(--tab);border:3px solid var(--white);border-radius:10px 0 0 10px;color:var(--tab-text);font-size:21px;font-weight:700;display:flex;align-items:center;justify-content:center;text-align:center;line-height:1.2;box-shadow:0 0 0 2px var(--panel-frame)}
.nav-tab.is-active{background:var(--white);color:var(--orange);height:86px;width:155px;box-shadow:-2px 0 0 2px var(--panel-frame);z-index:3}

/* panel */
.panel-frame{left:162px;top:282px;width:1028px;height:585px;background:var(--panel-frame);border-radius:16px}
.panel{left:177px;top:297px;width:1000px;height:558px;background:var(--white);border-radius:8px}
.page-title{left:230px;top:312px;font-family:"Handlee",cursive;font-size:44px;color:#4d5a4a}
.page-subtitle{left:230px;top:362px;font-size:30px;font-weight:800;color:var(--orange)}

/* form */
.label{font-size:17px;color:#444;text-align:right}
.select{height:21px;border:1px solid var(--field-border);background:var(--field-bg);font-size:16px;color:#555;padding-left:3px;line-height:19px}
.select::after{content:"";position:absolute;right:2px;top:2px;width:16px;height:15px;background:#d6d9d6 linear-gradient(transparent,transparent);border-left:1px solid var(--field-border)}
.select span.chev{position:absolute;right:6px;top:7px;width:0;height:0;border-left:4px solid transparent;border-right:4px solid transparent;border-top:5px solid #555;z-index:1}
.text-input{height:21px;border:1px solid var(--field-border);background:var(--white)}
.small-btn{height:15px;background:var(--panel-frame);color:var(--white);font-size:10px;font-weight:700;text-align:center;line-height:15px}
.range-dash{left:828px;top:427px;width:16px;height:2px;background:#555}
.continue{left:886px;top:477px;width:180px;height:50px;background:var(--panel-frame);border-radius:4px;color:var(--white);font-size:30px;font-weight:700;text-align:center;line-height:48px}

/* listings */
.listing{top:549px;width:178px}
.listing-image{height:93px;border:2px solid var(--orange);display:flex;align-items:center;justify-content:center;font-size:21px;color:#666}
.listing-text{position:absolute;left:24px;font-size:12.5px;line-height:15.5px;color:#333;white-space:nowrap}
.listing-arrow{position:absolute;left:0}
.print-link{right:16px;top:879px;font-size:11px;color:#a0a8a0;letter-spacing:.5px}
</style>
</head>
<body>

<header>
  <div class="abs hero" role="img" aria-label="Photo of a family relaxing on green grass"></div>
  <div class="abs brand"><span class="brand-mark"></span>TradeNest</div>
  <div class="abs tagline-band"></div>
  <p class="abs tagline">The place to sell. The place to buy.</p>
  <span class="abs login" style="left:685px">USER NAME</span>
  <span class="abs login-input" style="left:760px"></span>
  <span class="abs login" style="left:895px">PASSWORD</span>
  <span class="abs login-input" style="left:968px"></span>
  <span class="abs signin">SIGN IN</span>
</header>

<div class="abs panel-frame"></div>
<div class="abs panel"></div>

<nav>
  <div class="abs nav-tab" style="top:285px">Home</div>
  <div class="abs nav-tab is-active" style="top:377px">Property<br>Search</div>
  <div class="abs nav-tab" style="top:477px">How<br>It Works</div>
  <div class="abs nav-tab" style="top:567px">My<br>Account</div>
  <div class="abs nav-tab" style="top:660px">Contact</div>
</nav>

<main>
  <h1 class="abs page-title">Property</h1>
  <h2 class="abs page-subtitle">SEARCH PAGE</h2>

  <form>
    <span class="abs label" style="left:288px;top:414px;width:112px">Property Type:</span>
    <div class="abs select" style="left:412px;top:416px;width:116px">Any<span class="chev"></span></div>
    <span class="abs label" style="left:288px;top:438px;width:46px">State:</span>
    <div class="abs select" style="left:340px;top:440px;width:188px">Any<span class="chev"></span></div>
    <span class="abs label" style="left:288px;top:465px;width:60px">Suburb:</span>
    <div class="abs text-input" style="left:352px;top:465px;width:101px"></div>
    <div class="abs small-btn" style="left:459px;top:469px;width:58px">Refresh</div>
    <div class="abs small-btn" style="left:522px;top:469px;width:61px">clear</div>

    <span class="abs label" style="left:604px;top:414px">Price Range:</span>
    <div class="abs select" style="left:710px;top:416px;width:115px">Any<span class="chev"></span></div>
    <div class="abs range-dash"></div>
    <div class="abs select" style="left:845px;top:416px;width:115px">Any<span class="chev"></span></div>
    <span class="abs label" style="left:604px;top:441px">Bedrooms:</span>
    <div class="abs select" style="left:710px;top:442px;width:115px">Any<span class="chev"></span></div>
    <span class="abs label" style="left:604px;top:466px">Bathrooms:</span>
    <div class="abs select" style="left:710px;top:467px;width:115px">Any<span class="chev"></span></div>
    <span class="abs label" style="left:604px;top:492px">Carspaces:</span>
    <div class="abs select" style="left:710px;top:493px;width:115px">Any<span class="chev"></span></div>
    <div class="abs continue">continue</div>
  </form>

  <section>
    <article class="abs listing" style="left:201px">
      <div class="listing-image">image here</div>
    </article>
    <article class="abs listing" style="left:394px">
      <div class="listing-image">image here</div>
    </article>
    <article class="abs listing" style="left:586px">
      <div class="listing-image">image here</div>
    </article>
    <article class="abs listing" style="left:780px">
      <div class="listing-image">image here</div>
    </article>
    <article class="abs listing" style="left:973px">
      <div class="listing-image">image here</div>
    </article>
  </section>

  <!-- listing details -->
  <div class="abs" style="left:201px;top:642px">
    <svg class="listing-arrow" width="14" height="190" style="top:4px"><path d="M7 2 L13 14 H9 V88 H5 V14 H1 Z" fill="var(--orange)"/><path d="M7 186 L13 174 H9 V96 H5 V174 H1 Z" fill="var(--panel-frame)" stroke="none"/><g stroke="var(--white)" stroke-width="3"><line x1="3" y1="112" x2="11" y2="112"/><line x1="3" y1="130" x2="11" y2="130"/><line x1="3" y1="148" x2="11" y2="148"/></g></svg>
    <p class="listing-text" style="top:4px">The House I'm Swapping<br>Bed: 2&nbsp; Bath: 1<br>Type: Single Family<br>Asking Price: $130,000<br>In: Orlando, FL</p>
    <p class="listing-text" style="top:96px">Want To House Swap With<br>Bed: NA&nbsp; Bath: NA<br>Type: Single Family<br>In: fredericksburg, VA<br>Price Range:<br>$1 - No Maximum</p>
  </div>
  <div class="abs" style="left:394px;top:642px">
    <svg class="listing-arrow" width="14" height="190" style="top:4px"><path d="M7 2 L13 14 H9 V88 H5 V14 H1 Z" fill="var(--orange)"/><path d="M7 186 L13 174 H9 V96 H5 V174 H1 Z" fill="var(--panel-frame)"/><g stroke="var(--white)" stroke-width="3"><line x1="3" y1="112" x2="11" y2="112"/><line x1="3" y1="130" x2="11" y2="130"/><line x1="3" y1="148" x2="11" y2="148"/></g></svg>
    <p class="listing-text" style="top:4px">The House I'm Swapping<br>Bed: 2&nbsp; Bath: 1<br>Type: Single Family<br>Asking Price: $130,000<br>In: Orlando, FL</p>
    <p class="listing-text" style="top:96px">Want To House Swap With<br>Bed: NA&nbsp; Bath: NA<br>Type: Single Family<br>In: fredericksburg, VA<br>Price Range:<br>$1 - No Maximum</p>
  </div>
  <div class="abs" style="left:586px;top:642px">
    <svg class="listing-arrow" width="14" height="190" style="top:4px"><path d="M7 2 L13 14 H9 V88 H5 V14 H1 Z" fill="var(--orange)"/><path d="M7 186 L13 174 H9 V96 H5 V174 H1 Z" fill="var(--panel-frame)"/><g stroke="var(--white)" stroke-width="3"><line x1="3" y1="112" x2="11" y2="112"/><line x1="3" y1="130" x2="11" y2="130"/><line x1="3" y1="148" x2="11" y2="148"/></g></svg>
    <p class="listing-text" style="top:4px">The House I'm Swapping<br>Bed: 2&nbsp; Bath: 1<br>Type: Single Family<br>Asking Price: $130,000<br>In: Orlando, FL</p>
    <p class="listing-text" style="top:96px">Want To House Swap With<br>Bed: NA&nbsp; Bath: NA<br>Type: Single Family<br>In: fredericksburg, VA<br>Price Range:<br>$1 - No Maximum</p>
  </div>
  <div class="abs" style="left:780px;top:642px">
    <svg class="listing-arrow" width="14" height="190" style="top:4px"><path d="M7 2 L13 14 H9 V88 H5 V14 H1 Z" fill="var(--orange)"/><path d="M7 186 L13 174 H9 V96 H5 V174 H1 Z" fill="var(--panel-frame)"/><g stroke="var(--white)" stroke-width="3"><line x1="3" y1="112" x2="11" y2="112"/><line x1="3" y1="130" x2="11" y2="130"/><line x1="3" y1="148" x2="11" y2="148"/></g></svg>
    <p class="listing-text" style="top:4px">The House I'm Swapping<br>Bed: 2&nbsp; Bath: 1<br>Type: Single Family<br>Asking Price: $130,000<br>In: Orlando, FL</p>
    <p class="listing-text" style="top:96px">Want To House Swap With<br>Bed: NA&nbsp; Bath: NA<br>Type: Single Family<br>In: fredericksburg, VA<br>Price Range:<br>$1 - No Maximum</p>
  </div>
  <div class="abs" style="left:973px;top:642px">
    <svg class="listing-arrow" width="14" height="190" style="top:4px"><path d="M7 2 L13 14 H9 V88 H5 V14 H1 Z" fill="var(--orange)"/><path d="M7 186 L13 174 H9 V96 H5 V174 H1 Z" fill="var(--panel-frame)"/><g stroke="var(--white)" stroke-width="3"><line x1="3" y1="112" x2="11" y2="112"/><line x1="3" y1="130" x2="11" y2="130"/><line x1="3" y1="148" x2="11" y2="148"/></g></svg>
    <p class="listing-text" style="top:4px">The House I'm Swapping<br>Bed: 2&nbsp; Bath: 1<br>Type: Single Family<br>Asking Price: $130,000<br>In: Orlando, FL</p>
    <p class="listing-text" style="top:96px">Want To House Swap With<br>Bed: NA&nbsp; Bath: NA<br>Type: Single Family<br>In: fredericksburg, VA<br>Price Range:<br>$1 - No Maximum</p>
  </div>
</main>

<footer>
  <span class="abs print-link">PRINTER FRIENDLY VERSION</span>
</footer>

</body>
</html>
```